Upscale business cards needed for family office

We would like professional business cards created for employees of our family office. Relatively simple and straightforward, but also with a unique element to set them apart. Probably stick with neutral and simple colors that mesh well with the colors in the logo. We need space for the traditional elements, including name, title, address, email/phone number.

Industry/Entity Type

Business

Contact Information for Business Card

Space for name, title, phone number, email, address

```html
<!DOCTYPE html>
<html lang="en">
<head>
<meta charset="utf-8">
<title>Harlow &amp; Pine — Business Cards</title>
<link rel="stylesheet" href="https://fonts.googleapis.com/css2?family=Montserrat:wght@400;500;700&display=swap">
<style>
  :root {
    --bg: #e6e4e2;
    --brand-blue: #0a90c0;
    --card-white: #ffffff;
    --frame-grey: #a9adb0;
    --ink-dark: #4f5a63;
    --ink-grey: #6b6f73;
    --mark-grey: #8a8f94;
  }
  * { box-sizing: border-box; margin: 0; padding: 0; }
  html, body {
    width: 1200px; height: 1189px; overflow: hidden;
    background: var(--bg);
    font-family: "Montserrat", Arial, sans-serif;
  }
  .sheet {
    position: relative; width: 1200px; height: 1189px;
  }
  .card {
    position: absolute; left: 250px; width: 700px; height: 400px;
    box-shadow: 0 6px 18px rgba(0,0,0,0.12);
  }
  .card-front { top: 150px; background: var(--brand-blue); }
  .card-back  { top: 640px; background: var(--card-white); }
  .card-frame {
    position: absolute; inset: 18px;
    border: 2px solid var(--card-white);
  }
  .card-back .card-frame { border-color: var(--frame-grey); }

  .wordmark {
    position: absolute; display: flex; align-items: center; gap: 14px;
    font-weight: 700; font-size: 28px; letter-spacing: 0.5px; white-space: nowrap;
  }
  .wordmark-square { width: 30px; height: 30px; flex: none; }
  .card-front .wordmark {
    left: 50%; top: 50%; transform: translate(-50%, -50%); color: var(--card-white);
  }
  .card-front .wordmark-square { background: var(--card-white); }
  .card-back .wordmark {
    left: 60px; top: 200px; transform: translateY(-50%); color: var(--ink-dark); font-size: 25px;
  }
  .card-back .wordmark-square { background: var(--mark-grey); }

  .divider {
    position: absolute; left: 340px; top: 120px; width: 2px; height: 165px;
    background: var(--frame-grey);
  }
  .contact {
    position: absolute; left: 372px; top: 110px; color: var(--ink-grey);
  }
  .contact-name {
    color: var(--brand-blue); font-weight: 700; font-size: 24px; letter-spacing: 0.5px; line-height: 1;
  }
  .contact-title { font-size: 17px; margin-top: 2px; }
  .contact-address { font-size: 17px; line-height: 1.3; margin-top: 18px; }
  .contact-lines { margin-top: 6px; font-size: 17px; }
  .contact-line { display: flex; align-items: center; gap: 8px; line-height: 1.4; }
  .icon {
    width: 20px; height: 18px; background: var(--brand-blue);
    display: inline-flex; align-items: center; justify-content: center; flex: none;
  }
</style>
</head>
<body>
<main class="sheet">
  <section class="card card-front" aria-label="Card front">
    <div class="card-frame"></div>
    <div class="wordmark"><span class="wordmark-square"></span>Harlow &amp; Pine</div>
  </section>

  <section class="card card-back" aria-label="Card back">
    <div class="card-frame"></div>
    <div class="wordmark"><span class="wordmark-square"></span>Harlow &amp; Pine</div>
    <div class="divider"></div>
    <div class="contact">
      <p class="contact-name">JOHN SMITH</p>
      <p class="contact-title">Maneger</p>
      <p class="contact-address">Your Address,2nd Ste<br>Fernbrook, Avalon 1234</p>
      <div class="contact-lines">
        <p class="contact-line">
          <span class="icon"><svg width="12" height="12" viewBox="0 0 24 24"><path fill="#fff" d="M6.6 10.8a15 15 0 0 0 6.6 6.6l2.2-2.2a1 1 0 0 1 1-.25 11.4 11.4 0 0 0 3.6.57 1 1 0 0 1 1 1V20a1 1 0 0 1-1 1A17 17 0 0 1 3 4a1 1 0 0 1 1-1h3.5a1 1 0 0 1 1 1c0 1.250.2 2.45.57 3.57a1 1 0 0 1-.25 1z"/></svg></span>
          123 456 7890
        </p>
        <p class="contact-line">
          <span class="icon"><svg width="13" height="10" viewBox="0 0 26 20"><rect x="1" y="1" width="24" height="18" fill="none" stroke="#fff" stroke-width="2"/><path d="M1 1l12 10L25 1" fill="none" stroke="#fff" stroke-width="2"/></svg></span>
          your@yourcompany.com
        </p>
      </div>
    </div>
  </section>
</main>
</body>
</html>
```